New profile page for existing party website

For the party website 'Brindlepost' we need a new design for the user profile page.

The page should show
* a profile picture
* basic information like name, age and city
* music styles he/she likes
* links to their Facebook profile and website
* a bio (HTML content)
* events they plan to go to
* past events
* pictures

Challenge is that some users may have little information (just their name) while others have a huge description, lots of foto's, events, etc.

Please visit http://www.brindlepost.example and http://www.brindlepost.example/users/tobias

Target Market(s)

Men and women between 18 and 35

Industry/Entity Type

Night Club

Number of Pages Required

2 page

Font styles to use
Other font styles liked:
• Roboto

Requirements
Must have
• Please design how the page looks with a fully filled out profile and with an empty profile.
• It should fit well with the existing website.
• Include designs for both for small screens (mobile) and large screens (tablet, desktop).
Nice to have
• UX design on how to collapse or paginate sections.
• Interactive effects would be a bonus.
Should not have
• The page should not have subnavigation like menus or tabs.

```html
<!DOCTYPE html>
<html lang="nl">
<head>
<meta charset="utf-8">
<title>Brindlepost – Profiel</title>
<link href="https://fonts.googleapis.com/css2?family=Roboto:wght@400;500;700&display=swap" rel="stylesheet">
<style>
:root{
  --black:#000;
  --band:#333333;
  --white:#fff;
  --light:#efefef;
  --ink:#222;
  --muted:#8a8a8a;
  --line:#d6d6d6;
  --badge:rgba(60,60,60,.85);
  --accent:#e2233a;
}
*{box-sizing:border-box;margin:0;padding:0}
html,body{width:677px;height:1200px;overflow:hidden}
body{position:relative;background:var(--white);font-family:'Roboto',Arial,sans-serif;color:var(--ink)}
.abs{position:absolute}

/* header */
.site-header{position:absolute;left:0;top:0;width:677px;height:62px;background:var(--black)}
.brand{position:absolute;left:48px;top:20px;color:var(--white);font-size:21px;font-weight:500;display:flex;align-items:center;gap:7px}
.brand-dot{width:10px;height:10px;border-radius:50%;background:var(--white)}
.main-nav{position:absolute;left:260px;top:32px;display:flex;gap:17px}
.main-nav a{color:var(--white);font-size:9.6px;text-decoration:none;letter-spacing:.2px}
.account-btn{position:absolute;left:528px;top:27px;width:68px;height:22px;border:1px solid var(--white);border-radius:2px;color:var(--white);font-size:8px;display:flex;align-items:center;justify-content:center}
.search-btn{position:absolute;left:602px;top:27px;width:25px;height:22px;border:1px solid var(--white);border-radius:2px;display:flex;align-items:center;justify-content:center}

/* profile band */
.profile{position:absolute;left:0;top:62px;width:677px;height:202px;background:var(--band);color:var(--white)}
.avatar{position:absolute;left:53px;top:22px;width:150px;height:150px;border-radius:50%;border:3px solid var(--white);background:radial-gradient(circle at 50% 35%,#b58363 0%,#8c5b3c 35%,#c9b9a8 70%,#e5ddd2 100%)}
.profile-name{position:absolute;left:229px;top:38px;font-size:15px;font-weight:500;letter-spacing:.3px}
.profile-meta{position:absolute;left:229px;top:63px;font-size:9px;line-height:19.5px;color:#f0f0f0}
.profile-links{position:absolute;left:229px;top:143px;display:flex;gap:24px;font-size:10.5px}
.profile-links span{display:flex;align-items:center;gap:8px}
.slider-arrow{position:absolute}

/* intro */
.section-title{font-size:14.5px;font-weight:500;text-align:center;letter-spacing:.2px;color:#2a2a2a}
.intro-title{position:absolute;left:0;top:294px;width:677px}
.intro-text{position:absolute;left:48px;top:318px;width:581px;font-size:7.8px;line-height:12.3px;color:var(--muted);text-align:center}

/* info */
.info{position:absolute;left:0;top:385px;width:677px;height:247px;background:var(--light)}
.info-title{position:absolute;left:48px;top:46px;font-size:13px;font-weight:500;color:#2a2a2a}
.info-text{position:absolute;left:48px;top:70px;width:300px;font-size:7.9px;line-height:13.2px;color:var(--muted);text-align:justify}
.info-text p+p{margin-top:6px}
.video{position:absolute;left:365px;top:40px;width:262px;height:160px;background:var(--white);border:1px solid var(--line);box-shadow:0 1px 4px rgba(0,0,0,.3)}
.video-media{position:absolute;left:6px;top:5px;width:249px;height:148px;background:linear-gradient(135deg,#2a3f8a 0%,#6a3a7a 40%,#b0504a 70%,#3a2a5a 100%)}
.video-controls{position:absolute;left:0;bottom:0;width:100%;height:20px;background:#111}
.play{position:absolute;left:111px;top:60px}

/* events */
.events-title{position:absolute;left:0;top:658px;width:677px}
.event{position:absolute;top:693px;width:180px}
.event-photo{width:180px;height:109px;border:1px solid var(--line);padding:2px;background:var(--white)}
.event-photo div{width:100%;height:100%}
.date-badge{position:absolute;left:4px;top:29px;width:27px;height:54px;background:var(--badge);color:var(--white);text-align:center}
.date-badge .day{font-size:10.5px;font-weight:500;margin-top:5px}
.date-badge .mon{font-size:6px;font-weight:500}
.date-badge .year{font-size:7.5px;font-weight:500;margin-top:6px}
.event-name{margin-top:13px;font-size:8.5px;letter-spacing:.2px;color:#333}
.event-text{margin-top:5px;font-size:6.3px;line-height:9.8px;color:var(--muted);text-align:justify}
.read-more{display:block;margin-top:6px;font-size:6.6px;color:#333}

/* photos */
.photos{position:absolute;left:0;top:894px;width:673px;height:246px;background:var(--light)}
.photos-title{position:absolute;left:0;top:26px;width:655px}
.gallery{position:absolute;left:49px;top:64px;width:579px;height:157px;display:flex}
.gallery div{flex:1;height:100%}

/* footer */
.site-footer{position:absolute;left:0;top:1146px;width:677px;height:54px;background:var(--black);color:var(--white);text-align:center}
.footer-links{margin-top:17px;font-size:6.6px;font-weight:500}
.copyright{margin-top:6px;font-size:6.4px}
</style>
</head>
<body>

<header class="site-header">
  <div class="brand"><span class="brand-dot"></span>Brindlepost</div>
  <nav class="main-nav">
    <a href="#">HOME</a><a href="#">AGENDA</a><a href="#">FREE TICKETS</a><a href="#">PHOTOS</a><a href="#">NEWS</a>
  </nav>
  <div class="account-btn">MY ACCOUNT</div>
  <div class="search-btn"><svg width="10" height="10" viewBox="0 0 10 10"><circle cx="4" cy="4" r="3" fill="none" stroke="#fff" stroke-width="1.4"/><line x1="6.2" y1="6.2" x2="9" y2="9" stroke="#fff" stroke-width="1.6"/></svg></div>
</header>

<section class="profile">
  <svg class="slider-arrow" style="left:24px;top:87px" width="12" height="24" viewBox="0 0 12 24"><polyline points="11,1 1,12 11,23" fill="none" stroke="#bbb" stroke-width="1.2"/></svg>
  <div class="avatar" role="img" aria-label="Profielfoto van de fotograaf"></div>
  <h1 class="profile-name">KESTREL LENS STUDIO</h1>
  <div class="profile-meta">
    <div>Member since: May 24, 2006 &nbsp;|&nbsp; Age: 34 &nbsp;|&nbsp; City: Amsterdam &nbsp;|&nbsp; Music: Latin / Salsa</div>
    <div>Function:Head promotions, photograper, communication, marketing, and sales.</div>
    <div>Active since: jan 2006</div>
    <div>Shoots: 500 and counting</div>
  </div>
  <div class="profile-links">
    <span><svg width="15" height="15" viewBox="0 0 16 16"><circle cx="8" cy="8" r="7.5" fill="#fff"/><path d="M8 .5v15M.5 8h15M8 .5c-3 3-3 12 0 15M8 .5c3 3 3 12 0 15" stroke="#333" stroke-width=".9" fill="none"/></svg>Circle</span>
    <span><svg width="12" height="15" viewBox="0 0 12 15"><rect x="2" y="2" width="8" height="11" rx="1.5" fill="none" stroke="#fff" stroke-width="1.4"/><line x1="4.5" y1="5.5" x2="7.5" y2="5.5" stroke="#fff" stroke-width="1.2"/></svg>Circle</span>
  </div>
  <svg class="slider-arrow" style="left:629px;top:87px" width="12" height="24" viewBox="0 0 12 24"><polyline points="1,1 11,12 1,23" fill="none" stroke="#bbb" stroke-width="1.2"/></svg>
</section>

<h2 class="section-title intro-title">WIL JIJ FOTOGRAFEREN VOOR BRINDLEPOST?</h2>
<p class="intro-text">Als je uitgaan leuk vindt, makkelijk bent in de omgang en uiteraard houdt van fotograferen, biedt Brindlepost je de kans een kijkje te nemen in de wereld van de partyfotografie. Door de inzet van de fotografen is Brindlepost uitgegroeid tot een van de meest toonaangevende partysites van Nederland. De betrouwbaarheid, de hoge kwaliteit van de foto's en het coveren van de belangrijkste evenementen maakt van Brindlepost een van de best bezochte websites in ons vakgebied.</p>

<section class="info">
  <h2 class="info-title">BELANGRIJK INFORMATIE</h2>
  <div class="info-text">
    <p>Fotograferen voor Brindlepost is op vrijwillige basis. Je kan kiezen waar en wanneer je uitgaat en foto's maakt, maar een vaste inbreng word wel van je verwacht. Hoe meer je voor Brindlepost doet, hoe meer ervaring je opdoet met de camera en hoe beter je word. Hierdoor kan je weer naar interessantere feesten en festivals.</p>
    <p>Wat je wel krijgt is gratis entree voor een evenement en soms ook andere voordelen zoals gratis drankjes... Je gaat meestal met ze tweetjes op pad en ontmoet veel nieuwe mensen zoals DJ's en organisatoren. Hoe meer je voor Brindlepost.nl werkt hoe meer ervaring je er ook uit zal halen. De beste fotografen doen de leukste en de meest uitdagende evenementen bijvoorbeeld: Lumina Hall, Outer Pulse, Sunfold Weekend,</p>
  </div>
  <div class="video">
    <div class="video-media" role="img" aria-label="Videobeeld van een groep feestgangers op een festival">
      <svg class="play" width="28" height="28" viewBox="0 0 28 28"><circle cx="14" cy="14" r="13" fill="rgba(0,0,0,.55)" stroke="#fff" stroke-width="1"/><polygon points="11,8 20,14 11,20" fill="#fff"/></svg>
      <div class="video-controls">
        <svg width="249" height="20" viewBox="0 0 249 20">
          <circle cx="10" cy="10" r="4.5" fill="none" stroke="#fff" stroke-width="1"/><polygon points="9,8 12,10 9,12" fill="#fff"/>
          <polygon points="27,8 30,8 33,5 33,15 30,12 27,12" fill="var(--accent)"/>
          <rect x="37" y="7" width="20" height="6" fill="var(--accent)" opacity=".8"/>
          <rect x="64" y="9" width="136" height="2" fill="#666"/><rect x="64" y="9" width="40" height="2" fill="var(--accent)"/>
          <text x="205" y="12.5" fill="#ccc" font-size="5.5" font-family="Roboto,sans-serif">01:30 / 04:55</text>
          <rect x="228" y="7" width="6" height="5" fill="none" stroke="#fff" stroke-width=".9"/>
          <circle cx="241" cy="10" r="3" fill="none" stroke="#fff" stroke-width="1.4"/>
        </svg>
      </div>
    </div>
  </div>
</section>

<h2 class="section-title events-title">EVENTS OF THE PAST</h2>

<article class="event" style="left:49px">
  <div class="event-photo"><div role="img" aria-label="Festivalfoto van twee feestgangers" style="background:linear-gradient(135deg,#3c2a8a,#7a2a6a 50%,#2a4a3a)"></div></div>
  <div class="date-badge"><div class="day">02</div><div class="mon">JUN</div><div class="year">2016</div></div>
  <h3 class="event-name">FESTIVAL SOL VIVO 2016</h3>
  <p class="event-text">Lorem Ipsum has been the industry's standard dummy text ever since the 1500s, when an unknown printer took a galley of type and scrambled it to make a type specimen book.</p>
  <a class="read-more">Read More &raquo;</a>
</article>
<article class="event" style="left:249px">
  <div class="event-photo"><div role="img" aria-label="Festivalfoto van een juichende menigte" style="background:linear-gradient(135deg,#6a5a4a,#b58a6a 50%,#4a3a2a)"></div></div>
  <div class="date-badge"><div class="day">02</div><div class="mon">JUN</div><div class="year">2016</div></div>
  <h3 class="event-name">FESTIVAL SOL VIVO 2016</h3>
  <p class="event-text">Lorem Ipsum has been the industry's standard dummy text ever since the 1500s, when an unknown printer took a galley of type and scrambled it to make a type specimen book.</p>
  <a class="read-more">Read More &raquo;</a>
</article>
<article class="event" style="left:448px">
  <div class="event-photo"><div role="img" aria-label="Festivalfoto van een groep vrienden" style="background:linear-gradient(135deg,#5a2a2a,#8a3a3a 50%,#2a2a2a)"></div></div>
  <div class="date-badge"><div class="day">02</div><div class="mon">JUN</div><div class="year">2016</div></div>
  <h3 class="event-name">FESTIVAL SOL VIVO 2016</h3>
  <p class="event-text">Lorem Ipsum has been the industry's standard dummy text ever since the 1500s, when an unknown printer took a galley of type and scrambled it to make a type specimen book.</p>
  <a class="read-more">Read More &raquo;</a>
</article>

<section class="photos">
  <h2 class="section-title photos-title">PHOTOS</h2>
  <svg class="slider-arrow" style="left:29px;top:134px" width="11" height="22" viewBox="0 0 11 22"><polyline points="10,1 1,11 10,21" fill="none" stroke="#999" stroke-width="1.1"/></svg>
  <div class="gallery">
    <div role="img" aria-label="Feestgangers in oranje op straat" style="background:linear-gradient(160deg,#8a6a5a,#d0702a 60%,#b08a6a)"></div>
    <div role="img" aria-label="Feestganger in oranje jas met witte hoed" style="background:linear-gradient(160deg,#6a4a3a,#e0702a 60%,#5a4a3a)"></div>
    <div role="img" aria-label="Twee feestgangers voor grachtenpanden" style="background:linear-gradient(160deg,#9a8a7a,#d06a2a 55%,#2a2a2a)"></div>
    <div role="img" aria-label="Portret van twee feestgangers" style="background:linear-gradient(160deg,#4a2a1a,#8a5a3a 50%,#1a1a1a)"></div>
  </div>
  <svg class="slider-arrow" style="left:634px;top:134px" width="11" height="22" viewBox="0 0 11 22"><polyline points="1,1 10,11 1,21" fill="none" stroke="#999" stroke-width="1.1"/></svg>
</section>

<footer class="site-footer">
  <div class="footer-links">CONTACT &nbsp;|&nbsp; GEBRUIKERSVOORWAARDEN &nbsp;|&nbsp; PRIVACY POLICY</div>
  <div class="copyright">Copyright © 2016. All Rights Reserved</div>
</footer>

</body>
</html>
```